Brochure for financial planning firm

I need a brochure designed that will be folded into three panels idealy. I will provide the copy, logo, and some of the pictures.

Our primary business is finding investors for large-scale real estate developments.

Some of the pictures will have to come from outside this website given the file sizes. Please click the following link to download pictures of projects we have raised money for:

https://files.tarnuvex.net/share/7QmW2rLp94ZxKdTbYhVcNs3EaUfJ8gGo?view=open

Target Market(s)

People Ages 30 to 75. That are unsatisfied with their retirement investments

Industry/Entity Type

Financial

Requirements
Must have
• Addition to copy:
• To recieve information on our latest investments visit www.cloverpathsavings.ca
• Contact info:
• Tarrowby Wealth Management Inc.
• 4 Pellam Rd. W.
• Suite K300
• Hamilton, ON K2R 7T5
• Office: (905) 463-2918
• www.tarrowbywm.com
• The brochure must have somewhere printed on it near our contact info: RBQT Lic # 40963

```html
<!DOCTYPE html>
<html lang="en">
<head>
<meta charset="utf-8">
<title>Syndicated Mortgages – Tri-fold Brochure Inside Spread</title>
<link rel="stylesheet" href="https://fonts.googleapis.com/css2?family=Tinos:ital,wght@0,400;0,700;1,400;1,700&display=swap">
<style>
  :root {
    --page-bg: #f3f2f3;
    --paper: #ffffff;
    --paper-shade: #f6f6f7;
    --ink: #333336;
    --heading-ink: #3b3a40;
    --teal: #2f8a78;
    --teal-bright: #3fb3a0;
    --teal-light: #63c7b7;
    --teal-deep: #2a9682;
    --slate: #45424f;
    --slate-dark: #2f2d38;
    --fold: rgba(0,0,0,0.06);
    --photo-sky: #8fb4d6;
    --photo-brick: #8a5a4c;
    --photo-stone: #c9b48e;
    --photo-green: #6d8a3e;
  }
  * { box-sizing: border-box; margin: 0; padding: 0; }
  html, body {
    width: 1200px; height: 1000px; overflow: hidden;
    background: var(--page-bg);
    font-family: "Tinos", "Times New Roman", serif;
    color: var(--ink);
  }
  .brochure {
    position: absolute; left: 60px; top: 150px;
    width: 1080px; height: 700px;
    background: var(--paper);
    box-shadow: 0 12px 30px rgba(0,0,0,0.18);
    overflow: hidden;
  }
  .panel {
    position: absolute; top: 0; width: 360px; height: 700px;
  }
  .panel--left { left: 0; }
  .panel--middle { left: 360px; background: var(--paper-shade); }
  .panel--right { left: 720px; }
  .fold-line {
    position: absolute; top: 0; width: 1px; height: 700px; background: var(--fold); z-index: 5;
  }
  .decor, .photo { position: absolute; left: 0; top: 0; width: 1080px; height: 700px; }
  .decor { z-index: 1; }
  .photo { z-index: 0; }
  .copy { position: absolute; z-index: 3; font-size: 14.5px; line-height: 1.22; }
  .copy p { margin-bottom: 9px; }
  .section-title {
    font-size: 19px; font-weight: 700; letter-spacing: 0.5px;
    color: var(--heading-ink); text-transform: uppercase; margin-bottom: 8px;
  }
  .section-title .accent { color: var(--teal); }
  .copy--intro { left: 28px; top: 34px; width: 306px; }
  .copy--benefits { left: 388px; top: 112px; width: 300px; }
  .benefit-list { list-style: none; margin-top: 18px; }
  .benefit { position: relative; padding-left: 38px; margin-bottom: 22px; }
  .benefit-title {
    font-size: 15px; font-weight: 700; text-transform: uppercase;
    color: var(--heading-ink); letter-spacing: 0.3px;
  }
  .benefit-title .accent { color: var(--teal); }
  .tick { position: absolute; left: 0; top: 36px; width: 24px; height: 24px; }
  .copy--testimonial { left: 748px; top: 262px; width: 306px; }
  .testimonial-quote { font-size: 14.5px; }
  .testimonial-author { font-style: italic; font-weight: 700; margin-top: 6px; }
</style>
</head>
<body>
<main class="brochure">
  <div class="panel panel--left"></div>
  <div class="panel panel--middle"></div>
  <div class="panel panel--right"></div>

  <svg class="photo" viewBox="0 0 1080 700" aria-hidden="false">
    <defs>
      <linearGradient id="townhouse-tones" x1="0" y1="0" x2="0" y2="1">
        <stop offset="0" stop-color="var(--photo-sky)"/>
        <stop offset="0.35" stop-color="var(--photo-stone)"/>
        <stop offset="0.8" stop-color="#8f7a5c"/>
        <stop offset="1" stop-color="var(--photo-green)"/>
      </linearGradient>
      <linearGradient id="condo-tones" x1="0" y1="0" x2="1" y2="1">
        <stop offset="0" stop-color="#5f8fd0"/>
        <stop offset="0.45" stop-color="var(--photo-brick)"/>
        <stop offset="1" stop-color="var(--photo-green)"/>
      </linearGradient>
    </defs>
    <polygon role="img" aria-label="Photo of a modern townhouse development with landscaped lawn"
      points="0,420 340,420 360,470 360,700 0,700" fill="url(#townhouse-tones)"/>
    <polygon role="img" aria-label="Photo of a brick mid-rise condominium building with balconies"
      points="790,0 1010,0 1010,170 930,200 790,150" fill="url(#condo-tones)"/>
  </svg>

  <svg class="decor" viewBox="0 0 1080 700" aria-hidden="true">
    <!-- slate bands across the top fold -->
    <polygon points="450,0 720,0 720,85 560,30" fill="var(--slate)"/>
    <polygon points="720,0 790,0 790,150 720,85" fill="var(--slate-dark)"/>
    <polygon points="1010,0 1080,0 1080,250 930,200 1010,170" fill="var(--slate-dark)"/>
    <!-- teal shapes along the bottom -->
    <polygon points="0,540 0,700 190,700" fill="var(--teal-light)" opacity="0.75"/>
    <polygon points="260,700 320,560 400,700" fill="var(--teal-deep)"/>
    <polygon points="300,700 360,600 440,700" fill="var(--teal-bright)" opacity="0.85"/>
    <path d="M 360 640 Q 560 610 720 700 L 360 700 Z" fill="var(--teal-light)"/>
    <path d="M 360 640 Q 560 610 720 700 L 700 700 Q 560 630 360 660 Z" fill="var(--teal-deep)" opacity="0.7"/>
  </svg>

  <div class="fold-line" style="left:360px"></div>
  <div class="fold-line" style="left:720px"></div>

  <section class="copy copy--intro">
    <h2 class="section-title">Syndicated <span class="accent">Mortgages</span></h2>
    <p>The simplest way to describe a syndicated mortgage is that it is a mortgage where two or more people loan their money in the form of one mortgage to another party.</p>
    <p>As a syndicated mortgage investor you become the bank! In other words, when you invest in a syndicated mortgage offered by Tarrowby Wealth Management you are lending your money to a reputable real estate developer for a set interest rate.</p>
    <p>You might be thinking that lending mortgages are only for people with really deep pockets but in fact, if you have even $25,000 sitting in an account a mortgage investment is something you could take advantage of. RRSP, TFSA, RRIF, LIRA’s, and LIF’s are only some of the account types that are eligible for syndicated mortgage investments.</p>
  </section>

  <section class="copy copy--benefits">
    <p>There are many reasons why banks use mortgages as their preferred investments, here are just a few of those reasons and why you might want to think about adding a syndicated mortgage investment to your portfolio:</p>
    <ul class="benefit-list">
      <li class="benefit">
        <svg class="tick" viewBox="0 0 24 24" aria-hidden="true"><circle cx="12" cy="12" r="12" fill="var(--teal-bright)"/><path d="M6.5 12.5 L10.5 16 L17.5 8.5" fill="none" stroke="#fff" stroke-width="2.6" stroke-linecap="round" stroke-linejoin="round"/></svg>
        <h3 class="benefit-title">Security <span class="accent">of Principle</span></h3>
        <p>Your investment is registered against physical real estate at the Land Registry Office. This doesn’t mean it’s a guaranteed investment, but it definitely reduces the risk of loss! No mutual fund or stock portfolio can do that.</p>
      </li>
      <li class="benefit">
        <svg class="tick" viewBox="0 0 24 24" aria-hidden="true"><circle cx="12" cy="12" r="12" fill="var(--teal-bright)"/><path d="M6.5 12.5 L10.5 16 L17.5 8.5" fill="none" stroke="#fff" stroke-width="2.6" stroke-linecap="round" stroke-linejoin="round"/></svg>
        <h3 class="benefit-title">A Predictable <span class="accent">Rate of Return</span></h3>
        <p>With a syndicated mortgage investment you know exactly what you are entitled to earn from your investment because your rate of interest is written right into your contract with the borrower. No more ups and downs of the stock market.</p>
      </li>
      <li class="benefit">
        <svg class="tick" viewBox="0 0 24 24" aria-hidden="true"><circle cx="12" cy="12" r="12" fill="var(--teal-bright)"/><path d="M6.5 12.5 L10.5 16 L17.5 8.5" fill="none" stroke="#fff" stroke-width="2.6" stroke-linecap="round" stroke-linejoin="round"/></svg>
        <h3 class="benefit-title">Term <span class="accent">Investment Periods</span></h3>
        <p>A syndicated mortgage investment can range between a few months to about five years, depending on the project being built.</p>
      </li>
    </ul>
  </section>

  <section class="copy copy--testimonial">
    <h2 class="section-title">Testimonials</h2>
    <p class="testimonial-quote">My husband and I had been looking for an alternative to investing in mutual funds and the stock market for a while. The unpredictability of our mutual funds was something we were sick and tired of. When we were introduced to the syndicated mortgage investments offered by Tarrowby Wealth Management, I thought the rate of return was too good to be true, that is until we attended one of their introductory seminars. Now that we invested some of our money with Tarrowby I don’t cringe when my investment statements come in the mail, and we can sleep at night.</p>
    <p class="testimonial-author">Marina Coletti, Client</p>
  </section>
</main>
</body>
</html>
```